Theater Production Company in Las Vegas

Needing a business card for a theater production company in Las Vegas. We are a full service theatrical production company specializing in Las Vegas entertainment, national
touring shows, and one-off events. From gorilla marketing teams to large scale productions... we do it,and better than anyone.

We like the feel of something hand made and organic.The final design should be creative and communicate that we specialize in theater and special events. We would like to have a design with a front and back.

Hi All,

I want to elaborate on the style of the design that we are hoping for. We are a theater production company in Las Vegas, so the competition is fierce and having a clever business card is incredibly important. 

I am attached a few concepts of a "feel" that would be nice to have conveyed in our card. We love the "worn and vintage" feel that is often seen in antique circus posters. Traditionally, the circus posters are clustered and full of copy - I want a more simplified version of that. Not so cluttered, but with that worn feel. Perhaps even having the card printed on recycled paper to give that textured feel to the visual. 

Example 1 - has a fun worn look, with stars. Some version of this for the back of the card would be fun.
Example 2 - Same things, cool worn feel. Perhaps a small star at the center of the swirl and a little softer on the "grunge".
Example 3 - Has the circus ornament but the colors are nice, not overpowering and again, has that worn feel.
Example 4 - This design isn't as "tight" and cluttered. Has some room to breathe.
Example 5 - I am really liking the look of the this and the above, especially for the back of the card. 

But just to reiterate, the front and face of the card needs to be clear and easy to read. 

Hi Designers, 

I have posted an update so you can have a clearer understanding of what we are needing. I have also increased the funding.

Thank you in advance for your help.

Bridget

Industry/Entity Type

Marketing

Requirements
Must have
• We want to assign creative license. We are creative and hate to be limited by restrictions. Have fun!

The attached files are our logo. One of the files is a business card design that I love. Just a sample of our taste.
Nice to have
• We would like to incorporate: Crafters of Spectacle
as our tagline. I like a vintage, worn feel to the look of designs. Just the word "purveyor" sounds vintage.

```html
<!DOCTYPE html>
<html lang="en">
<head>
<meta charset="utf-8">
<title>Amber Lantern Productions – Business Card</title>
<link rel="stylesheet" href="https://fonts.googleapis.com/css2?family=Cinzel:wght@400;500&family=Lato:wght@400;700&display=swap">
<style>
  :root {
    --backdrop: #1c1c1e;
    --card: #4a4644;
    --card-light: #57524f;
    --card-dark: #3d3937;
    --brush: #3a3634;
    --ink-light: #f3f0ea;
    --ink-dark: #1d1b1a;
    --gold: #e8dcb0;
  }
  * { margin: 0; padding: 0; box-sizing: border-box; }
  html, body {
    width: 1200px; height: 426px; overflow: hidden;
    background: var(--backdrop);
  }
  .canvas { position: relative; width: 1200px; height: 426px; }
  .card {
    position: absolute; top: 63px; width: 512px; height: 296px;
    border-radius: 16px;
    background: radial-gradient(ellipse at 50% 40%, var(--card-light), var(--card) 55%, var(--card-dark));
    overflow: hidden;
  }
  .card--front { left: 72px; }
  .card--back { left: 608px; }
  .brush-texture {
    position: absolute; top: 14px; left: 150px; width: 340px; height: 120px;
    background: radial-gradient(ellipse at 55% 45%, var(--brush), transparent 70%);
    opacity: .7;
  }
  .wordmark {
    position: absolute; left: 0; right: 0; text-align: center;
    font-family: "Cinzel", serif; font-weight: 400;
  }
  .wordmark__name { display: block; font-size: 40px; line-height: 1; letter-spacing: 1px; }
  .wordmark__sub { display: block; font-size: 11px; line-height: 1; letter-spacing: 14px; margin-top: 12px; padding-left: 14px; }
  .card--front .wordmark { top: 98px; color: var(--ink-light); }
  .card--back .wordmark { top: 124px; color: var(--ink-dark); }
  .contact {
    position: absolute; left: 0; right: 0; top: 196px; text-align: center;
    color: var(--ink-light); font-family: "Lato", sans-serif;
  }
  .contact__name { font-family: "Cinzel", serif; font-size: 19px; letter-spacing: .5px; }
  .contact__role { font-family: "Lato", sans-serif; font-size: 13px; }
  .contact__address { font-size: 13px; margin-top: 10px; }
  .contact__lines { font-size: 13px; margin-top: 4px; display: flex; justify-content: center; gap: 8px; align-items: center; }
  .contact__lines span { display: inline-flex; align-items: center; gap: 3px; }
  .icon { width: 10px; height: 10px; fill: var(--ink-light); }
  .icon--mail { fill: none; stroke: var(--ink-light); stroke-width: 1.2; }
  .contact__web { font-size: 15px; font-weight: 700; margin-top: 4px; }
  .tagline {
    position: absolute; left: 0; right: 0; top: 248px; text-align: center;
    font-family: "Cinzel", serif; font-size: 21px; color: var(--gold); letter-spacing: .5px;
  }
  .tagline small { font-size: 14px; }
</style>
</head>
<body>
<main class="canvas">
  <section class="card card--front">
    <div class="brush-texture" role="img" aria-label="Faint grunge brush-stroke texture"></div>
    <div class="wordmark">
      <span class="wordmark__name">Amber Lantern</span>
      <span class="wordmark__sub">PRODUCTIONS</span>
    </div>
    <div class="contact">
      <p><span class="contact__name">SHANNON BRIDGET,</span> <span class="contact__role">Designation</span></p>
      <p class="contact__address">Lantern Row, Suite 500, Las Vegas, NV 89101</p>
      <p class="contact__lines">
        <span><svg class="icon" viewBox="0 0 10 10"><rect x="2" y="0" width="6" height="10" rx="1"/></svg>702 555 0143</span>
        <span><svg class="icon" viewBox="0 0 10 10"><path d="M2 0l2 2-1 2c1 1 2 2 3 3l2-1 2 2-2 2C4 10 0 6 0 2z"/></svg>702 555 0144</span>
        <span><svg class="icon icon--mail" viewBox="0 0 10 10"><rect x="0.6" y="2" width="8.8" height="6"/><path d="M0.6 2l4.4 3 4.4-3"/></svg>hello@amberlantern.com</span>
      </p>
      <p class="contact__web">www.AMBERLANTERN.com</p>
    </div>
  </section>

  <section class="card card--back">
    <div class="brush-texture" role="img" aria-label="Faint grunge brush-stroke texture"></div>
    <div class="wordmark">
      <span class="wordmark__name">Amber Lantern</span>
      <span class="wordmark__sub">PRODUCTIONS</span>
    </div>
    <p class="tagline">CRAFTERS <small>OF</small> SPECTACLE</p>
  </section>
</main>
</body>
</html>
```